Business cards real estate company

We need a design for a business card. It is a company that specializes in real estate sales. There should be space for a photo of the respective employee as well as the website and telephone number on it. Design should be noble, innovative.

Contact Information for Business Card

Website, Name, Position, Telefonnummer

Requirements
Must have
• Photo, logo

```html
<!DOCTYPE html>
<html lang="en">
<head>
<meta charset="utf-8">
<title>Domivista Business Card</title>
<link rel="stylesheet" href="https://fonts.googleapis.com/css2?family=Arimo:wght@400;700&display=swap">
<style>
  :root {
    --green: #78bd43;
    --green-dark: #63a532;
    --white: #ffffff;
    --ink: #2b2b2b;
    --stage: #2a2a2a;
    --suit: #2d3e6b;
  }
  * { margin: 0; padding: 0; box-sizing: border-box; }
  html, body { width: 1200px; height: 988px; overflow: hidden; }
  body {
    background: var(--stage);
    font-family: "Arimo", Arial, sans-serif;
    position: relative;
  }
  .card {
    position: absolute;
    width: 700px;
    height: 400px;
    border-radius: 26px;
    overflow: hidden;
  }
  .card-back {
    left: 90px;
    top: 64px;
    background: var(--green);
    display: flex;
    align-items: center;
    justify-content: center;
  }
  .card-back .wordmark {
    color: var(--white);
    font-weight: 700;
    font-size: 104px;
    letter-spacing: -1px;
  }
  .card-front {
    left: 410px;
    top: 524px;
    background: var(--white);
  }
  .card-front .wordmark {
    position: absolute;
    left: 46px;
    top: 96px;
    color: var(--green);
    font-weight: 700;
    font-size: 62px;
    letter-spacing: -0.5px;
  }
  .name-band {
    position: absolute;
    left: 0;
    top: 200px;
    width: 470px;
    height: 70px;
    background: var(--green);
    padding: 12px 0 0 96px;
    color: var(--white);
  }
  .name-band .person-name {
    font-weight: 700;
    font-size: 28px;
    letter-spacing: 0.5px;
    line-height: 1;
  }
  .name-band .person-role {
    font-size: 16px;
    margin-top: 5px;
  }
  .contact-list {
    position: absolute;
    left: 96px;
    top: 292px;
    list-style: none;
    color: var(--ink);
    font-size: 17px;
  }
  .contact-list li {
    display: flex;
    align-items: center;
    gap: 10px;
    height: 28px;
  }
  .contact-list svg { width: 15px; height: 15px; flex: none; }
  .portrait {
    position: absolute;
    right: 0;
    bottom: 0;
    width: 290px;
    height: 340px;
    background: linear-gradient(180deg, #e9e4e0 0%, #c9a28a 30%, #f3f4f6 52%, var(--suit) 70%, #22315a 100%);
    border-top-left-radius: 120px;
  }
</style>
</head>
<body>
  <section class="card card-back">
    <span class="wordmark">Domivista</span>
  </section>

  <section class="card card-front">
    <span class="wordmark">Domivista</span>
    <div class="name-band">
      <div class="person-name">DANIEL REYES</div>
      <div class="person-role">Owner</div>
    </div>
    <ul class="contact-list">
      <li>
        <svg viewBox="0 0 16 16" aria-hidden="true"><path fill="#78bd43" d="M3.6 1.2l2.2 2.6-1.3 1.6c.9 2 2.2 3.3 4.2 4.2l1.6-1.3 2.6 2.2-1.3 2.3C7 12.6 3.4 9 1.3 2.5z"/></svg>
        555-210-3846
      </li>
      <li>
        <svg viewBox="0 0 16 16" aria-hidden="true"><rect x="1" y="3" width="14" height="10" rx="1" fill="#78bd43"/><path d="M1.5 3.5L8 9l6.5-5.5" stroke="#fff" stroke-width="1.3" fill="none"/></svg>
        info@domivista.com
      </li>
      <li>
        <svg viewBox="0 0 16 16" aria-hidden="true"><circle cx="8" cy="8" r="7" fill="#78bd43"/><path d="M1 8h14M8 1c-3 3.5-3 10.5 0 14M8 1c3 3.5 3 10.5 0 14" stroke="#fff" stroke-width="1" fill="none"/></svg>
        www.domivista.com
      </li>
    </ul>
    <div class="portrait" role="img" aria-label="Portrait photo of the employee in a navy suit and white shirt"></div>
  </section>
</body>
</html>
```